Ecommerce Software Provider Needs A Fresh Look For Website

We are looking for a fresh, new look for our existing ecommerce software service. We provide an ecommerce software targeted at small business owners called "QuickvaleShop" and our existing website can be seen at http://www.quickvaleshop.example.

QuickvaleShop helps small business owners build their online store instantly without any coding. We focus on not just building "online stores" but PROFITABLE online stores. As such, we focus on tools and features that help our clients create online stores that convert.

The "feel" we want to portray to our clients are as below:

- Powerful
- Easy to use
- Can start quickly
- Successful
- Profitable

We are open to pretty much any color scheme or feel. The only thing we absolutely want to retain is our company logo which uses a shade of green and black.

So, this is pretty much a "free reign" kind of project. Let your imagination and design juices run wild! :-)

```html
<!DOCTYPE html>
<html lang="en">
<head>
<meta charset="utf-8">
<title>QuickvaleShop – Ecommerce Software</title>
<link href="https://fonts.googleapis.com/css2?family=Open+Sans:wght@400;600;700&display=swap" rel="stylesheet">
<style>
:root{
  --green:#3aa935;
  --green-dark:#2a8a27;
  --ink:#222;
  --text:#444;
  --muted:#888;
  --light:#f4f4f4;
  --line:#e2e2e2;
  --footer:#232323;
  --footer-text:#bbb;
  --white:#fff;
}
*{box-sizing:border-box;margin:0;padding:0}
html,body{width:1200px;height:2290px;overflow:hidden}
body{font-family:"Open Sans",Arial,sans-serif;color:var(--text);background:var(--white);position:relative}
a{text-decoration:none;color:inherit}
.abs{position:absolute}

/* header */
.topbar{top:0;left:0;width:1200px;height:52px;border-bottom:1px solid var(--line)}
.brand{left:149px;top:10px;font-size:26px;font-weight:700;color:var(--ink);display:flex;align-items:center;gap:8px}
.brand .dot{width:22px;height:22px;border-radius:50%;background:var(--green)}
.toplinks{right:149px;top:14px;display:flex;gap:26px;align-items:center;font-size:12px;font-weight:600;color:var(--ink);text-transform:uppercase}
.btn-signup{background:var(--green);color:var(--white);padding:4px 12px;border-radius:3px}
.mainnav{top:52px;left:0;width:1200px;height:42px;background:#fafafa;border-bottom:1px solid var(--line)}
.mainnav ul{list-style:none;display:flex;justify-content:space-between;margin:0 149px;line-height:42px;font-size:14px;color:var(--ink)}

/* hero */
.hero{top:94px;left:0;width:1200px;height:479px;background:linear-gradient(135deg,#5a4a30 0%,#3c3a2a 40%,#6b5a3a 70%,#2e2b22 100%)}
.hero-title{left:149px;top:52px;font-size:42px;font-weight:700;color:var(--white);white-space:nowrap}
.pay-names{left:149px;top:136px;display:flex;gap:28px;font-size:22px;font-weight:700;color:var(--white)}
.hero-cta{left:534px;top:130px;width:340px;height:46px;background:var(--green);color:var(--white);font-size:14px;white-space:nowrap;border-radius:4px;display:flex;align-items:center;justify-content:center;border:1px solid var(--green-dark)}
.hero-collage{left:126px;top:200px;width:424px;height:265px;background:linear-gradient(120deg,#d9d2c2,#9bb0c8 50%,#c6a48a);opacity:.55}
.hero-cart{left:698px;top:181px;width:424px;height:275px;border-radius:6px;background:linear-gradient(160deg,rgba(255,255,255,.35),rgba(255,255,255,.15))}
.dots{left:565px;top:448px;display:flex;gap:8px}
.dots span{width:12px;height:12px;border-radius:50%;background:var(--white)}
.dots span:first-child{background:var(--green)}

/* features */
.features{top:573px;left:0;width:1200px;height:274px;background:linear-gradient(#fff,#ececec);border-bottom:1px solid var(--line)}
.feat-line{left:309px;top:66px;width:602px;height:6px;background:var(--green)}
.feat-icon{width:58px;height:58px;border-radius:50%;background:var(--green);border:4px solid #cfe8cd;top:40px;display:flex;align-items:center;justify-content:center}
.feat{width:250px;top:124px;text-align:center}
.feat h3{font-size:20px;font-weight:600;color:var(--ink);margin-bottom:8px;white-space:nowrap}
.feat p{font-size:13.5px;line-height:21px}
.feat a{display:block;margin-top:10px;font-size:14px;color:var(--green)}

/* reasons */
.reasons-title{top:890px;left:0;width:1200px;text-align:center;font-size:22px;font-weight:700;color:var(--green);letter-spacing:.5px}
.reason{width:420px;display:flex;gap:22px}
.reason .ico{flex:none;width:52px;height:52px;border-radius:50%;background:#eee;display:flex;align-items:center;justify-content:center}
.reason p{font-size:13.5px;line-height:20px;color:var(--text)}

/* promos */
.promos{top:1534px;left:0;width:1200px;height:264px;background:var(--light);border-top:1px solid var(--line);border-bottom:1px solid var(--line)}
.promo-divider{left:600px;top:40px;width:1px;height:190px;background:var(--line)}
.promo{width:420px;top:38px}
.promo h3{font-size:21px;line-height:28px;font-weight:700;color:var(--green);margin-bottom:14px}
.promo p{font-size:14px;line-height:21px}
.promo a{display:block;margin-top:14px;font-size:14px;color:var(--green)}

/* clients */
.clients{top:1820px;left:149px;width:902px;height:80px;display:flex;justify-content:space-between;align-items:center;color:#9a9a9a;font-size:26px;font-weight:700}
.clients .mark{width:52px;height:52px;border-radius:50%;background:#d6d6d6}

/* footer */
.footer{top:1923px;left:0;width:1200px;height:367px;background:var(--footer);color:var(--footer-text)}
.fcol{top:40px}
.fcol h4{font-size:17px;font-weight:600;color:var(--white);margin-bottom:14px}
.fcol ul{list-style:none;font-size:12.5px;line-height:31px}
.fcol .hl{color:var(--green);font-weight:700}
.copyright{left:149px;top:290px;font-size:11.5px;line-height:18px;color:#777}
.badge{left:800px;top:298px;width:118px;height:36px;background:#eaeaea;border-radius:3px}
.social{left:962px;top:300px;display:flex;gap:12px}
.social span{width:28px;height:28px;border-radius:50%;background:#555}
</style>
</head>
<body>

<header class="abs topbar">
  <div class="abs brand"><span>QuickvaleShop</span><span class="dot"></span></div>
  <nav class="abs toplinks"><a href="#">Contact Us</a><a href="#">Merchant Login</a><a class="btn-signup" href="#">Sign Up</a></nav>
</header>
<nav class="abs mainnav">
  <ul><li>Cart Features</li><li>Pricing</li><li>Credit Cards</li><li>Happy Clients Everywhere!</li><li>Ecommerce Templates</li><li>Free Live Chat</li><li>Ecommerce Blog</li></ul>
</nav>

<section class="abs hero" role="img" aria-label="Blurred shop interior photo background">
  <h1 class="abs hero-title">Build once, sell instantly in 3 places...</h1>
  <div class="abs pay-names"><span>Searchly Checkout</span><span>PayNorth</span></div>
  <a class="abs hero-cta" href="#">Click here &amp; start selling in less than 15 minutes</a>
  <div class="abs hero-collage" role="img" aria-label="Fan of online store template screenshots"></div>
  <div class="abs hero-cart" role="img" aria-label="Large white shopping cart illustration"></div>
  <div class="abs dots"><span></span><span></span><span></span><span></span></div>
</section>

<section class="abs features">
  <div class="abs feat-line"></div>
  <div class="abs feat-icon" style="left:280px"><svg width="26" height="26" viewBox="0 0 26 26"><rect x="3" y="3" width="20" height="20" rx="3" fill="none" stroke="#fff" stroke-width="3"/><path d="M3 10h20" stroke="#fff" stroke-width="3"/></svg></div>
  <div class="abs feat-icon" style="left:571px"><svg width="28" height="22" viewBox="0 0 28 22"><rect x="2" y="2" width="24" height="18" rx="2" fill="none" stroke="#fff" stroke-width="3"/><path d="M2 8h24" stroke="#fff" stroke-width="4"/></svg></div>
  <div class="abs feat-icon" style="left:882px"><svg width="24" height="24" viewBox="0 0 24 24"><rect x="2" y="2" width="20" height="20" rx="3" fill="none" stroke="#fff" stroke-width="3"/><path d="M9 8h8M9 12h8M9 16h5" stroke="#fff" stroke-width="2"/></svg></div>
  <div class="abs feat" style="left:214px"><h3>Beautiful Templates</h3><p>You need to attract attention within second or you've just lost your potential customer.</p><a href="#">See how →</a></div>
  <div class="abs feat" style="left:482px"><h3>Accept Payments Easily</h3><p>How should you let your customers pay you? credit card, PayNorth or Searchly</p><a href="#">Learn more →</a></div>
  <div class="abs feat" style="left:752px"><h3>Sell on Friendbook</h3><p>Whether you like it or not, Friendbook is here to stay.</p><a href="#">Find out how →</a></div>
</section>

<h2 class="abs reasons-title">TOP 10 REASONS WHY PEOPLE CHOOSE QUICKVALESHOP</h2>

<div class="abs reason" style="left:149px;top:975px"><span class="ico"><svg width="24" height="22" viewBox="0 0 24 22"><path d="M1 2h4l3 12h12l2-9H7" fill="none" stroke="#999" stroke-width="2"/><circle cx="10" cy="19" r="2" fill="#999"/><circle cx="18" cy="19" r="2" fill="#999"/></svg></span><p>Complete all-in-one solution comes with your store builder, shopping cart, payment integration, ecommerce hosting, internet marketing tools and MUCH more...</p></div>
<div class="abs reason" style="left:627px;top:975px"><span class="ico"><svg width="24" height="18" viewBox="0 0 24 18"><rect x="1" y="1" width="22" height="16" rx="2" fill="none" stroke="#999" stroke-width="2"/><path d="M1 6h22" stroke="#999" stroke-width="3"/></svg></span><p>Accept credit cards online with or without your own merchant account. Need a merchant account? We can offer you very competitive pricing as well</p></div>

<div class="abs reason" style="left:149px;top:1095px"><span class="ico"><svg width="22" height="22" viewBox="0 0 22 22"><circle cx="11" cy="11" r="9" fill="none" stroke="#999" stroke-width="2"/><path d="M6 11l4 4 6-8" fill="none" stroke="#999" stroke-width="2"/></svg></span><p>Everyone loves free traffic. Your store pages are search engine optimized so that you rank higher on Searchly, Findra &amp; Lookwise to tap into free search engine traffic</p></div>
<div class="abs reason" style="left:627px;top:1095px"><span class="ico"><svg width="22" height="22" viewBox="0 0 22 22"><circle cx="11" cy="7" r="5" fill="#999"/><path d="M2 21c1-6 17-6 18 0z" fill="#999"/></svg></span><p>Site protected by strongest SSL security &amp; proprietary order fraud prevention included FREE with every account to keep you and your customers safe</p></div>

<div class="abs reason" style="left:149px;top:1210px"><span class="ico"><svg width="22" height="22" viewBox="0 0 22 22"><path d="M19 11a8 8 0 1 1-3-6.2M17 1v5h-5" fill="none" stroke="#999" stroke-width="2"/></svg></span><p>Everyone loves free traffic. Your store pages are search engine optimized so that you rank higher on Searchly, Findra &amp; Lookwise to tap into free search engine traffic</p></div>
<div class="abs reason" style="left:627px;top:1210px"><span class="ico"><svg width="26" height="20" viewBox="0 0 26 20"><rect x="4" y="1" width="18" height="13" rx="1" fill="none" stroke="#999" stroke-width="2"/><path d="M1 18h24" stroke="#999" stroke-width="3"/></svg></span><p>With more than 60 beautiful ecommerce templates to choose from, building an attractive &amp; stylish store is simply easy</p></div>

<div class="abs reason" style="left:149px;top:1322px"><span class="ico"><svg width="16" height="24" viewBox="0 0 16 24"><rect x="1" y="1" width="14" height="22" rx="2" fill="none" stroke="#999" stroke-width="2"/><circle cx="8" cy="19" r="1.5" fill="#999"/></svg></span><p>Sometimes you just want things to be a certain way. QuickvaleShop is flexible to meet your needs. Heck, it's so flexible that you can even change every single word and image in your store!</p></div>
<div class="abs reason" style="left:627px;top:1322px"><span class="ico"><svg width="24" height="22" viewBox="0 0 24 22"><path d="M2 2h20v13H9l-5 5v-5H2z" fill="none" stroke="#999" stroke-width="2"/></svg></span><p>Super-responsive customer service from REAL people who will bend over backwards to help you out. You won't get any "standard answers" from us</p></div>

<div class="abs reason" style="left:149px;top:1428px"><span class="ico"><svg width="24" height="18" viewBox="0 0 24 18"><rect x="1" y="1" width="22" height="16" rx="2" fill="none" stroke="#999" stroke-width="2"/><circle cx="12" cy="9" r="3" fill="#999"/></svg></span><p>Super-competitive pricing. Unlike some of our competitors, we do NOT believe in having any hidden fees nor taking a percentage of your sales</p></div>
<div class="abs reason" style="left:627px;top:1428px"><span class="ico"><svg width="22" height="22" viewBox="0 0 22 22"><rect x="2" y="2" width="18" height="7" rx="1" fill="none" stroke="#999" stroke-width="2"/><rect x="2" y="13" width="18" height="7" rx="1" fill="none" stroke="#999" stroke-width="2"/></svg></span><p>Super-stable and lightning-fast ecommerce hosting with 99.9% uptime guarantee makes sure your store is available all the time. Never miss a sale because your store is down</p></div>

<section class="abs promos">
  <div class="abs promo-divider"></div>
  <div class="abs promo" style="left:149px"><h3>Shopping Cart<br>Software That Is Super Easy To Use...</h3><p>Building your ecommerce store? Don't worry. Our simple point-and-click system lets you set up online store in no time. What if you're an ecommerce expert? Then, you'll be pleased to know that QuickvaleShop suits you as well.</p><a href="#">See how →</a></div>
  <div class="abs promo" style="left:625px"><h3>At Last! A Shopping Cart Software<br>That Helps You Sell More...</h3><p>QuickvaleShop is one of the few ecommerce solutions that actually helps you to sell more. With built-in tools like our "people who bought this also bought this" feature, your store will literally urge people to buy more from you.</p><a href="#">See how →</a></div>
</section>

<div class="abs clients">
  <span class="mark"></span><span>Copivo</span><span>Bellardi</span><span>K-Clasp</span><span class="mark"></span><span>tqrm</span><span>Kanemori</span>
</div>

<footer class="abs footer">
  <div class="abs fcol" style="left:149px"><h4>QuickvaleShop.com</h4><ul><li>Shopping Cart Features</li><li>Plans &amp; Pricing</li><li class="hl">30-Day Free Trial</li><li>Sign Up Now!</li><li>Client Showcase</li></ul></div>
  <div class="abs fcol" style="left:309px;top:74px"><ul><li>Ecommerce Templates</li><li>See What Our Clients Say</li><li>Software Updates</li><li>Affiliates</li><li>About Us</li></ul></div>
  <div class="abs fcol" style="left:566px"><h4>Services</h4><ul><li>Accept Credit Cards</li><li>Payment Gateways</li><li>Logo Design</li><li>Ecommerce Web Design</li><li>FREE Live Chat Software</li><li>Shopping Portal</li></ul></div>
  <div class="abs fcol" style="left:815px"><h4>Contact Us</h4><ul style="line-height:24px"><li>USA: +1-555-010-4188</li><li>Australia: +61-3-5550-9790</li><li>International: +60-4-5550-0704</li><li>Chat With Us Live</li><li>Ecommerce Support / Email Us</li><li>Existing Merchants: Support Ticket System</li></ul></div>
  <p class="abs copyright">© Copyright 2001-2014 Brightlane Tech Sdn. Bhd. All rights reserved<br>QuickvaleShop is a registered trademark of Brightlane Tech Sdn. Bhd. View Privacy Policy<br>Ecommerce software, ecommerce solutions &amp; QuickvaleShop shopping cart software provider</p>
  <div class="abs badge"></div>
  <div class="abs social"><span></span><span></span><span></span><span></span></div>
</footer>

</body>
</html>
```